Software Company Business Card Design

We are looking for a business card design for a software, messaging & IT services company based in Australia.

Talvora Group is the holding company for 3 brands all offering technology based business solutions; Talvora, Brindle & Quillpad. Brand Identity = Friendly, Professional, Viable, Vibrant, Creative

We want our business card to reflect that we are an innovative market leader. The design should be clean, professional and original.

This design will be used for all 3 brands.

More information about our company can be found at: www.talvoragroup.example.au
www.brindle.example.au

Details we would like on the card:

Firstname Lastname
Position
Level 17, 482 Ormond Rd
North Sydney
NSW 2060
Phone: +61 2 5550 1738
Fax: +61 2 5550 1794
Mobile:
Email:
www.talvoragroup.example.au

Target Market(s)

Our business cards are given to B2B and industry professionals.

Industry/Entity Type

Business

Requirements
Must have
• The Business Card must include the same colours as the logo.
Nice to have
• We would like it to me double sided.

```html
<!DOCTYPE html>
<html lang="en">
<head>
<meta charset="utf-8">
<title>Talvora Group – Business Card</title>
<link rel="stylesheet" href="https://fonts.googleapis.com/css2?family=Noto+Sans:wght@400;600&display=swap">
<style>
  :root {
    --page: #ffffff;
    --card: #050505;
    --ink: #ffffff;
    --ink-soft: #d6d6d8;
    --accent: #9b93d6;
    --shape: #5a5a5c;
  }
  * { box-sizing: border-box; margin: 0; padding: 0; }
  html, body { width: 765px; height: 1200px; overflow: hidden; background: var(--page); }
  body { position: relative; font-family: "Noto Sans", sans-serif; color: var(--ink); }

  .card {
    position: absolute;
    left: 42px;
    width: 680px;
    height: 415px;
    background: var(--card);
    overflow: hidden;
  }
  .card--front { top: 80px; }
  .card--back { top: 575px; }

  .card__shape {
    position: absolute;
    right: -130px;
    top: 40px;
    width: 340px;
    height: 340px;
  }
  .card--back .card__shape { top: 90px; right: -160px; }

  .brand {
    position: absolute;
    left: 34px;
    top: 62px;
    display: flex;
    align-items: center;
    gap: 14px;
  }
  .brand__dot {
    width: 20px; height: 20px;
    border-radius: 50%;
    background: var(--accent);
  }
  .brand__name {
    font-size: 54px;
    font-weight: 400;
    letter-spacing: 1px;
    color: var(--ink);
    line-height: 1;
  }

  .person {
    position: absolute;
    left: 52px;
    top: 258px;
    font-size: 30px;
    line-height: 1.25;
  }
  .person__credential { font-size: 18px; }

  .address {
    position: absolute;
    left: 52px;
    top: 350px;
    font-size: 17px;
    line-height: 1.4;
    color: var(--ink-soft);
    font-style: normal;
  }

  .contacts {
    position: absolute;
    left: 26px;
    top: 26px;
    border-collapse: collapse;
    font-size: 24px;
  }
  .contacts th {
    text-align: left;
    font-weight: 600;
    width: 205px;
    padding: 0 0 38px;
    vertical-align: top;
  }
  .contacts td { padding: 0 0 38px; vertical-align: top; }
  .contacts td.contacts__email { font-size: 22px; }

  .website {
    position: absolute;
    left: 0; right: 0;
    bottom: 30px;
    text-align: center;
    font-size: 36px;
    letter-spacing: 0.5px;
  }
</style>
</head>
<body>

  <section class="card card--front" aria-label="Card front">
    <svg class="card__shape" viewBox="0 0 100 100" aria-hidden="true">
      <circle cx="50" cy="50" r="50" fill="var(--shape)"/>
    </svg>
    <div class="brand">
      <span class="brand__name">Talvora Group</span>
      <span class="brand__dot"></span>
    </div>
    <div class="person">
      <p class="person__name">Jordan Vale, <span class="person__credential">Ba. Comm</span></p>
      <p class="person__role">Director, Marketing</p>
    </div>
    <address class="address">Level 17, 482 Ormond Rd, North Sydney NSW 2060</address>
  </section>

  <section class="card card--back" aria-label="Card back">
    <svg class="card__shape" viewBox="0 0 100 100" aria-hidden="true">
      <circle cx="50" cy="50" r="50" fill="var(--shape)"/>
    </svg>
    <table class="contacts">
      <tr><th>Phone:</th><td>+61 2 5550 1738</td></tr>
      <tr><th>Fax:</th><td>+61 2 5550 1794</td></tr>
      <tr><th>Mobile:</th><td>+61 2 5550 1822</td></tr>
      <tr><th>Email:</th><td class="contacts__email">j.vale@talvoragroup.example.au</td></tr>
    </table>
    <p class="website">www.talvoragroup.example.au</p>
  </section>

</body>
</html>
```